A4 Menu needed for cafe - attached design

Need an A4 menu designed for our cafe.
I have attached our catering menu - I would like the new menu to be designed in the exact same way.

I have attached the text that needs to appear on the menu

Industry/Entity Type

Catering

```html
<!DOCTYPE html>
<html lang="en">
<head>
<meta charset="utf-8">
<title>Harbour Corner Menu</title>
<link rel="stylesheet" href="https://fonts.googleapis.com/css2?family=Arvo:wght@400;700&family=Bebas+Neue&family=Courier+Prime&display=swap">
<style>
  :root {
    --board: #08090d;
    --board-raised: #0f1014;
    --chalk: #ffffff;
    --lemon: #f7f3a1;
    --cocoa: #3b2f2f;
  }
  * { margin: 0; padding: 0; box-sizing: border-box; }
  html, body { width: 1200px; height: 927px; overflow: hidden; background: var(--board); }
  .menu-board {
    position: relative;
    width: 1200px;
    height: 927px;
    background: var(--board);
    color: var(--chalk);
    font-family: "Arvo", Georgia, serif;
    font-weight: 700;
  }
  .brand-panel {
    position: absolute;
    left: 473px; top: 0;
    width: 245px; height: 213px;
    background: var(--board-raised);
  }
  .brand {
    position: absolute;
    left: 508px; top: 18px;
    width: 185px; height: 162px;
    background: var(--lemon);
    display: flex;
    align-items: center;
    justify-content: center;
    gap: 8px;
  }
  .brand-dot {
    width: 14px; height: 14px;
    border-radius: 50%;
    background: var(--cocoa);
  }
  .brand-name {
    font-family: "Arvo", Georgia, serif;
    font-weight: 700;
    font-size: 17px;
    line-height: 1.2;
    color: var(--cocoa);
    text-align: center;
    letter-spacing: 1px;
    text-transform: uppercase;
  }
  .menu-label {
    position: absolute;
    left: 508px; top: 182px;
    width: 185px;
    text-align: center;
    font-family: "Courier Prime", "Courier New", monospace;
    font-weight: 400;
    font-size: 24px;
    color: var(--lemon);
  }
  .section-frame {
    position: absolute;
    border: 1.5px solid var(--chalk);
  }
  .section-frame--breakfast { left: 114px; top: 240px; width: 449px; height: 351px; }
  .section-frame--lunch { left: 637px; top: 240px; width: 449px; height: 351px; }
  .section-frame--light { left: 200px; top: 636px; width: 800px; height: 262px; }
  .section-banner {
    position: absolute;
    height: 44px;
  }
  .section-banner svg { position: absolute; inset: 0; }
  .section-banner h2 {
    position: relative;
    font-family: "Bebas Neue", "Arial Narrow", sans-serif;
    font-weight: 400;
    font-size: 31px;
    line-height: 46px;
    text-align: center;
    color: var(--chalk);
    letter-spacing: 0.5px;
  }
  .section-banner--breakfast { left: 166px; top: 219px; width: 341px; }
  .section-banner--lunch { left: 692px; top: 219px; width: 339px; }
  .section-banner--light { left: 430px; top: 614px; width: 339px; }
  .item-list {
    position: absolute;
    list-style: none;
    font-size: 15px;
    line-height: 26.4px;
  }
  .item { position: relative; white-space: nowrap; }
  .item-price { position: absolute; top: 0; }
  .item-list--breakfast { left: 167px; top: 282px; width: 360px; }
  .item-list--breakfast .item-price { left: 306px; }
  .item-list--breakfast .item-price--per-slice { left: 234px; }
  .item-list--lunch { left: 690px; top: 283px; width: 360px; }
  .item-list--lunch .item-price { left: 307px; }
  .item-list--lunch .item-price--split { left: 258px; }
  .item-list--light-left { left: 236px; top: 679px; width: 360px; }
  .item-list--light-left .item-price { left: 306px; }
  .item-list--light-right { left: 632px; top: 679px; width: 360px; }
  .item-list--light-right .item-price { left: 306px; }
</style>
</head>
<body>
<main class="menu-board">
  <div class="brand-panel"></div>
  <div class="brand">
    <span class="brand-dot"></span>
    <span class="brand-name">Harbour<br>Corner</span>
  </div>
  <div class="menu-label">menu</div>

  <section class="section-frame section-frame--breakfast"></section>
  <div class="section-banner section-banner--breakfast">
    <svg viewBox="0 0 341 44" width="341" height="44"><polygon points="1,1 340,1 324,22 340,43 1,43 17,22" fill="var(--board)" stroke="var(--lemon)" stroke-width="1.5"/></svg>
    <h2>Breakfast</h2>
  </div>
  <ul class="item-list item-list--breakfast">
    <li class="item">Toast<span class="item-price item-price--per-slice">per slice$2</span></li>
    <li class="item">Raisin Toast<span class="item-price item-price--per-slice">per slice$2</span></li>
    <li class="item">Egg Bacon and Cheese Roll<span class="item-price">$6.5</span></li>
    <li class="item">Veggie Brekky Wrap<span class="item-price">$6.5</span></li>
    <li class="item">Ham and Cheese French Toast<span class="item-price">$6.5</span></li>
    <li class="item">Ham and Cheese Toastie<span class="item-price">$5.5</span></li>
    <li class="item">Cheese and Tomato Toastie<span class="item-price">$5.5</span></li>
    <li class="item">Ham Cheese and Tomato Toastie<span class="item-price">$6</span></li>
    <li class="item">Cheese and tomato Croissant<span class="item-price">$6</span></li>
    <li class="item">Ham and Cheese Croissant<span class="item-price">$6.5</span></li>
    <li class="item">Plain Croissant<span class="item-price">$3.5</span></li>
  </ul>

  <section class="section-frame section-frame--lunch"></section>
  <div class="section-banner section-banner--lunch">
    <svg viewBox="0 0 339 44" width="339" height="44"><polygon points="1,1 338,1 322,22 338,43 1,43 17,22" fill="var(--board)" stroke="var(--lemon)" stroke-width="1.5"/></svg>
    <h2>Lunch</h2>
  </div>
  <ul class="item-list item-list--lunch">
    <li class="item">Pre made Sandwiches<span class="item-price item-price--split">$6.5 / $7.5</span></li>
    <li class="item">Pre made Focaccias<span class="item-price">$8.5</span></li>
    <li class="item">Pre made Wraps<span class="item-price">$7.5</span></li>
    <li class="item">Pre made Mini Rolls<span class="item-price">$4</span></li>
    <li class="item">Pre made Baguettes<span class="item-price">$9</span></li>
    <li class="item">Pre made Bagels<span class="item-price">$9</span></li>
    <li class="item">Fresh Salads made daily<span class="item-price">$9.5</span></li>
    <li class="item">Hot Chips<span class="item-price">$4.5</span></li>
    <li class="item">Plain Hamburger<span class="item-price">$7.5</span></li>
    <li class="item">Hamburger with the Lot<span class="item-price">$9</span></li>
    <li class="item">Chicken Schnitzel Burger<span class="item-price">$8.5</span></li>
  </ul>

  <section class="section-frame section-frame--light"></section>
  <div class="section-banner section-banner--light">
    <svg viewBox="0 0 339 44" width="339" height="44"><polygon points="1,1 338,1 322,22 338,43 1,43 17,22" fill="var(--board)" stroke="var(--lemon)" stroke-width="1.5"/></svg>
    <h2>Something Light</h2>
  </div>
  <ul class="item-list item-list--light-left">
    <li class="item">Mixed Yogurts<span class="item-price">$5.5</span></li>
    <li class="item">Granola and Fruit Yogurt<span class="item-price">$5.5</span></li>
    <li class="item">Chia Pudding<span class="item-price">$5.5</span></li>
    <li class="item">Bircher Muesli<span class="item-price">$5.5</span></li>
    <li class="item">Fruit Salad<span class="item-price">$5.5</span></li>
    <li class="item">Banana Bread<span class="item-price">$4.5</span></li>
  </ul>
  <ul class="item-list item-list--light-right">
    <li class="item">Muffins – made fresh daily<span class="item-price">$4.5</span></li>
    <li class="item">Slices<span class="item-price">$4</span></li>
    <li class="item">Cookies<span class="item-price">$4</span></li>
    <li class="item">Choc Crunch Energy Bite<span class="item-price">$4</span></li>
    <li class="item">Super Crunch Energy Bite<span class="item-price">$4</span></li>
    <li class="item">Chocolate Bar<span class="item-price">$3</span></li>
    <li class="item">Packet of Chips<span class="item-price">$3</span></li>
  </ul>
</main>
</body>
</html>
```